Qb Panes

We need a website design for a company based in Texas that specializes in doors and and windows.
Qb Pane is a leading window manufacturer of aluminum and vinyl windows, both serving the replacement and new construction markets. Qb Pane Inc. was created over 25 years ago when two existing window manufacturers with excellent reputations in their fields - merged. Qb Pane offers a complete line conforming to the needs of residential and commercial window markets.
The final design should be something that communicates professionalism and features they're key value propositions.
Example websites we like:
http://layouts.pebblecraft.example/zx/satchel/
http://layouts.pebblecraft.example/zx/splashyard/
http://layouts.pebblecraft.example/zx/rebuildr2/
This design should format the existing content to be more visually organized, improve the fonts to clearer and more readable, and make it easier for users to find services.
Brand guide is attached
Website images can be found here: https://docs.vaultcrate.example/7kRTmwQzLpXeBd
Target Market(s)
Windows
Number of Pages Required
1 page
Look and feel
Each slider illustrates characteristics of the customer's brand and the style your logo design should communicate.

```html
<!DOCTYPE html>
<html lang="en">
<head>
<meta charset="utf-8">
<title>Qb Panes — Doors and Windows, Texas</title>
<link rel="stylesheet" href="https://fonts.googleapis.com/css2?family=Rubik:wght@300;400;500;700&display=swap">
<style>
  :root {
    --gold: #d4b451;
    --ink: #1d1a14;
    --white: #ffffff;
    --accent-red: #b8243c;
    --teal: #3d6567;
    --hero-red: #e4604f;
    --paper: #ffffff;
  }
  * { box-sizing: border-box; margin: 0; padding: 0; }
  html, body { width: 1200px; height: 2634px; overflow: hidden; background: var(--paper); }
  body { position: relative; font-family: "Rubik", sans-serif; color: var(--ink); }
  .abs { position: absolute; }
  .photo { position: absolute; box-shadow: 0 22px 40px rgba(0,0,0,0.22); }
  .gold-panel { position: absolute; background: var(--gold); }
  .section-title { position: absolute; font-weight: 400; letter-spacing: 2px; color: var(--ink); line-height: 1; }
  .btn { position: absolute; display: flex; align-items: center; justify-content: center; color: var(--white); font-weight: 500; font-size: 19px; letter-spacing: 1px; background: var(--gold); }
  .btn--teal { background: var(--teal); }
  .link-underlined { position: absolute; font-size: 14px; color: var(--ink); border-bottom: 2px solid var(--accent-red); padding-bottom: 2px; }

  /* header */
  .site-header { left: 0; top: 0; width: 752px; height: 119px; }
  .brand { position: absolute; left: 43px; top: 22px; font-weight: 700; font-size: 46px; letter-spacing: 1px; line-height: 1; }
  .brand-place { position: absolute; left: 45px; top: 72px; font-size: 20px; }
  .header-phone { position: absolute; left: 448px; top: 48px; font-size: 14px; font-weight: 500; color: var(--white); letter-spacing: 1px; }
  .menu-toggle { position: absolute; left: 660px; top: 50px; }

  /* hero */
  .intro-rule { left: 43px; top: 223px; width: 53px; height: 2px; background: var(--ink); }
  .intro-text { left: 43px; top: 239px; width: 290px; font-size: 13px; line-height: 21px; }
  .hero-photo { left: 466px; top: 92px; width: 734px; height: 484px; background: linear-gradient(160deg, #f06c58 0%, #e05a48 45%, #c94a3c 100%); }
  .hero-title { left: 608px; top: 210px; width: 560px; font-size: 47px; font-weight: 400; line-height: 58px; letter-spacing: 2px; color: var(--white); }

  /* what you get */
  .interior-photo { left: 0; top: 604px; width: 592px; height: 380px; background: linear-gradient(180deg, #d9dde2 0%, #b9bcc0 55%, #b88b58 100%); z-index: 2; }
  .benefits-panel { left: 463px; top: 693px; width: 687px; height: 326px; z-index: 1; }
  .feature { position: absolute; width: 240px; text-align: center; font-size: 13px; }
  .feature svg { display: block; margin: 0 auto 10px; }

  /* workers */
  .worker { position: absolute; left: 216px; width: 400px; height: 71px; }
  .worker-thumb { position: absolute; left: 0; top: 0; width: 94px; height: 71px; }
  .worker-name { position: absolute; left: 110px; top: 10px; font-size: 12px; border-bottom: 2px solid var(--accent-red); padding-bottom: 2px; }
  .worker-role { position: absolute; left: 110px; top: 44px; font-size: 12px; }
  .grinder-photo { left: 750px; top: 1046px; width: 450px; height: 379px; background: radial-gradient(circle at 45% 45%, #6b5a3a 0%, #3f3c38 45%, #2a2d31 100%); }

  /* service */
  .facade-photo { left: 0; top: 1453px; width: 732px; height: 351px; background: linear-gradient(135deg, #b8322c 0%, #3d5c88 50%, #b8322c 100%); }
  .service-panel { left: 608px; top: 1510px; width: 548px; height: 323px; }
  .service-item { position: absolute; width: 170px; text-align: center; font-size: 13px; top: 1648px; }
  .service-item svg { display: block; margin: 0 auto 10px; }

  /* client */
  .quote-mark { left: 43px; top: 1943px; font-size: 34px; font-weight: 700; font-style: italic; line-height: 1; }
  .review-text { left: 43px; top: 1970px; width: 395px; font-size: 13px; font-weight: 500; line-height: 22px; }
  .reviewer-avatar { left: 43px; top: 2063px; width: 93px; height: 71px; background: linear-gradient(135deg, #c98f6a, #7d4e3a); }
  .reviewer-name { left: 154px; top: 2080px; font-size: 21px; font-weight: 500; }
  .door-photo { left: 468px; top: 1861px; width: 732px; height: 379px; background: linear-gradient(90deg, #1e1e1e 0%, #3a3326 35%, #5e5236 55%, #2a2720 80%, #141414 100%); }

  /* footer */
  .map-area { left: 0; top: 2269px; width: 732px; height: 365px; background: linear-gradient(135deg, #e8e4da 0%, #dfe6d6 50%, #bcd3ea 100%); }
  .footer-panel { left: 732px; top: 2311px; width: 468px; height: 323px; }
  .footer-brand { position: absolute; left: 18px; top: 22px; font-weight: 700; font-size: 45px; letter-spacing: 1px; }
  .footer-brand span { font-size: 20px; font-weight: 400; letter-spacing: 0; margin-left: 10px; }
  .contact-line { position: absolute; left: 18px; font-size: 14px; font-weight: 500; color: var(--white); letter-spacing: .5px; }
  .social { position: absolute; left: 260px; display: flex; align-items: center; gap: 8px; font-size: 15px; font-weight: 500; color: var(--ink); }
  .social i { display: block; width: 14px; height: 14px; border-radius: 50%; background: var(--ink); }
</style>
</head>
<body>

<header class="gold-panel site-header">
  <div class="brand">Company.</div>
  <div class="brand-place">Texas</div>
  <div class="header-phone">+ 012-345-67-89</div>
  <svg class="menu-toggle" width="24" height="14" viewBox="0 0 24 14" aria-label="Menu">
    <rect y="0" width="24" height="2" fill="#b8243c"/><rect y="6" width="24" height="2" fill="#b8243c"/><rect y="12" width="24" height="2" fill="#b8243c"/>
  </svg>
</header>

<div class="abs intro-rule"></div>
<p class="abs intro-text">Lorem Ipsum is simply dummy text of the printing and typesetting industry. Lorem Ipsum has been the industry's standard dummy text ever since the 1500s, when an unknown printer took a galley of type and scrambled it to make a type specimen book. It has survived not only five centuries, but also the leap into electronic typesetting, remaining essentially unchanged.</p>
<a class="link-underlined" style="left:43px;top:421px;">More detailed</a>

<div class="photo hero-photo" role="img" aria-label="Red modern building facade with balconies"></div>
<h1 class="abs hero-title">We make Doors and Windows in new generation</h1>
<div class="btn" style="left:608px;top:399px;width:284px;height:37px;">view catalog</div>

<div class="photo interior-photo" role="img" aria-label="Empty room with a large glass window facing a winter courtyard"></div>
<section class="gold-panel benefits-panel">
  <h2 class="section-title" style="left:205px;top:20px;font-size:46px;">What you get</h2>
  <div class="feature" style="left:90px;top:100px;">
    <svg width="34" height="40" viewBox="0 0 34 40" fill="none" stroke="#1d1a14" stroke-width="2"><path d="M6 38V2h22v36"/><path d="M6 2l14 6v30L6 38"/><circle cx="16" cy="22" r="1.5" fill="#1d1a14"/></svg>
    Lorem Ipsum is simply
  </div>
  <div class="feature" style="left:371px;top:100px;">
    <svg width="40" height="40" viewBox="0 0 40 40" fill="none" stroke="#1d1a14" stroke-width="2"><path d="M10 16a10 10 0 0 1 20 0z"/><path d="M7 16h26"/><circle cx="20" cy="23" r="6"/><path d="M6 39c1-8 7-10 14-10s13 2 14 10"/></svg>
    Lorem Ipsum is simply
  </div>
  <div class="feature" style="left:90px;top:205px;">
    <svg width="40" height="40" viewBox="0 0 40 40" fill="none" stroke="#1d1a14" stroke-width="2"><rect x="2" y="2" width="36" height="36"/><rect x="7" y="7" width="11" height="26"/><rect x="22" y="7" width="11" height="12"/><rect x="22" y="23" width="11" height="10"/></svg>
    Lorem Ipsum is simply
  </div>
  <div class="feature" style="left:371px;top:200px;">
    <svg width="44" height="44" viewBox="0 0 44 44" fill="none" stroke="#1d1a14" stroke-width="2"><circle cx="16" cy="28" r="9" stroke-dasharray="4 2"/><circle cx="16" cy="28" r="4"/><circle cx="31" cy="13" r="7" stroke-dasharray="3 2"/><circle cx="31" cy="13" r="3"/></svg>
    Lorem Ipsum is simply
  </div>
</section>

<h2 class="section-title" style="left:43px;top:1048px;font-size:48px;">Our professional workers</h2>
<div class="worker" style="top:1117px;">
  <div class="worker-thumb" role="img" aria-label="Worker at a workshop" style="background:linear-gradient(135deg,#5a6a78,#2f3a44);"></div>
  <div class="worker-name">Arlo Brennick</div><div class="worker-role">Position</div>
</div>
<div class="worker" style="top:1200px;">
  <div class="worker-thumb" role="img" aria-label="Worker team on site" style="background:linear-gradient(135deg,#7a5a3c,#2e2a28);"></div>
  <div class="worker-name">Dell Marrow</div><div class="worker-role">Position</div>
</div>
<div class="worker" style="top:1285px;">
  <div class="worker-thumb" role="img" aria-label="Worker using tools" style="background:linear-gradient(135deg,#8a9098,#3a4048);"></div>
  <div class="worker-name">Jory Vale</div><div class="worker-role">Position</div>
</div>
<div class="btn" style="left:326px;top:1390px;width:282px;height:35px;">in detail</div>
<div class="photo grinder-photo" role="img" aria-label="Worker in a hard hat grinding metal with sparks"></div>

<div class="photo facade-photo" role="img" aria-label="Red building facade with rows of angled windows"></div>
<section class="gold-panel service-panel" style="z-index:1;">
  <h2 class="section-title" style="left:0;width:548px;text-align:center;top:22px;font-size:46px;">Our service</h2>
</section>
<div class="service-item" style="left:624px;z-index:2;">
  <svg width="40" height="40" viewBox="0 0 40 40" fill="none" stroke="#1d1a14" stroke-width="2"><path d="M4 36L34 6v30z"/><path d="M14 30l10-10v10z"/><path d="M10 36v-4M16 36v-4M22 36v-4M28 36v-4"/></svg>
  Lorem Ipsum is simply
</div>
<div class="service-item" style="left:796px;z-index:2;">
  <svg width="40" height="40" viewBox="0 0 40 40" fill="none" stroke="#1d1a14" stroke-width="2"><path d="M6 34L24 16"/><path d="M22 8a7 7 0 0 0 10 10l-4-4 2-4z"/><path d="M8 6l4 2 16 16 4 8-8-4L8 12z"/></svg>
  Lorem Ipsum is simply
</div>
<div class="service-item" style="left:970px;z-index:2;">
  <svg width="42" height="40" viewBox="0 0 42 40" fill="none" stroke="#1d1a14" stroke-width="2"><rect x="3" y="10" width="36" height="26" rx="3"/><path d="M15 10V5h12v5"/><path d="M3 20h36"/><rect x="18" y="17" width="6" height="6"/></svg>
  Lorem Ipsum is simply
</div>
<div class="btn btn--teal" style="left:750px;top:1774px;width:283px;height:34px;z-index:2;">in detail</div>

<h2 class="section-title" style="left:43px;top:1883px;font-size:50px;">Our client</h2>
<div class="abs quote-mark">"</div>
<p class="abs review-text">Contrary to popular belief, Lorem Ipsum is not simply random text. It has roots in a piece of classical Latin literature from 45 BC, making it over 2000 years old.</p>
<div class="abs reviewer-avatar" role="img" aria-label="Client portrait"></div>
<div class="abs reviewer-name">Ina Lorre</div>
<a class="link-underlined" style="left:43px;top:2185px;font-size:18px;">All the reviews</a>
<div class="photo door-photo" role="img" aria-label="Dark wooden double door with a smart lock"></div>

<div class="abs map-area" role="img" aria-label="Road map of the United States"></div>
<footer class="gold-panel footer-panel">
  <div class="footer-brand">Company.<span>Texas</span></div>
  <div class="contact-line" style="top:92px;">+ 012-345-67-89</div>
  <div class="contact-line" style="top:125px;">Your address</div>
  <div class="contact-line" style="top:159px;">your@address.mail</div>
  <div class="contact-line" style="top:196px;">www.your site.com</div>
  <div class="social" style="top:106px;"><i></i>Lenscast</div>
  <div class="social" style="top:182px;"><i></i>Friendwall</div>
</footer>

</body>
</html>
```